Label Redesign For Hemp Oil Tincture Bottle*

I need a label redesigned for Marbleleaf Hemp, current bottle label and logo is attached. The current label doesn't standout, not sure if its the font size or colors on the existing label. It is very important to have on the label that this is a Premium Full Spectrum Hemp Oil that is 2000mg. Then after the label is redesigned and approved, I would need to packaging to be designed to match the approved label design.
This Hemp oil has a relaxing effect to help ease mental and emotional stress, tension and worry. The Omega Fatty Acids it contains also naturally improves your mood and overall brain function, causing you to feel more alert and focused. Hemp Oil helps with insomnia. Take some 2-3 hours before bedtime, you will feel relaxed yet aware of how tired you are that it will lead to a good night's sleep. Hemp Oil helps ease chronic pain and inflammation from conditions such as arthritis, fibromyalgia, lupus, and MS. As a pain relief supplement, it is a safer, natural, non-chemical and non-addictive alternative to prescription painkillers.

Target Market(s)

Adults

Industry/Entity Type

Supplement

Font styles to use
Serif
Sans Serif

Colors

Designer to choose colors to be used in the design.

Requirements
Must have
• All information thats on current label but where it says 750 in the front of the existing label, it needs to say 2000. The 2000 should be prominent on the label.

```html
<!DOCTYPE html>
<html lang="en">
<head>
<meta charset="utf-8">
<title>Marbleleaf Hemp – Tincture Label Set</title>
<link rel="stylesheet" href="https://fonts.googleapis.com/css2?family=Roboto:wght@400;700&family=Roboto+Condensed:wght@400;700&family=Tinos:wght@400;700&family=Great+Vibes&display=swap">
<style>
  :root{
    --page:#ffffff;
    --label:#f5f6ea;
    --ink:#222222;
    --green:#2f7d3e;
    --green-soft:#9fcf8c;
    --green-line:#5a9a6a;
    --pill:#8cc08a;
    --teal:#8fcfc4;
    --teal-soft:#d2ece4;
  }
  *{box-sizing:border-box;margin:0;padding:0}
  html,body{width:1001px;height:1200px;overflow:hidden;background:var(--page)}
  .canvas{position:relative;width:1001px;height:1200px}
  .label{position:absolute;top:430px;width:270px;height:340px;background:var(--label);
    box-shadow:0 0 0 1px #e2e4d4;font-family:"Roboto",sans-serif;color:var(--ink)}
  .label--left{left:50px}
  .label--front{left:366px}
  .label--right{left:682px}
  .label__pill{position:absolute;left:50%;bottom:18px;transform:translateX(-50%);
    width:90px;height:20px;border-radius:10px;background:var(--pill)}

  /* left panel */
  .info{position:absolute;left:28px;top:34px;width:218px}
  .info h3{font-family:"Roboto Condensed",sans-serif;font-weight:700;font-size:11.5px;margin-top:8px}
  .info h3:first-child{margin-top:0}
  .info p{font-size:10.5px;line-height:1.45}
  .info h4{font-family:"Roboto Condensed",sans-serif;font-weight:700;font-size:11.5px;line-height:1.35;
    text-transform:uppercase;margin-top:12px;width:120px}
  .splash{position:absolute;border-radius:50%}
  .splash--side{left:150px;top:182px;width:80px;height:80px;
    background:radial-gradient(circle,var(--teal) 0%,var(--teal-soft) 60%,transparent 72%)}

  /* front panel */
  .brand{position:absolute;top:30px;left:0;width:100%;text-align:center}
  .brand__dot{display:block;width:22px;height:22px;border-radius:50%;background:var(--green-soft);margin:0 auto 6px}
  .brand__name{font-family:"Roboto Condensed",sans-serif;font-weight:700;font-size:25px;color:var(--green);letter-spacing:-.3px}
  .brand__tag{position:absolute;right:16px;top:24px;background:var(--green-soft);color:#fff;
    font-family:"Tinos",serif;font-size:10px;padding:2px 6px;border-radius:8px}
  .splash--front{left:55px;top:105px;width:160px;height:130px;
    background:radial-gradient(ellipse,var(--teal) 0%,var(--teal-soft) 58%,transparent 72%)}
  .product{position:absolute;top:118px;left:0;width:100%;text-align:center}
  .product__line{font-family:"Roboto Condensed",sans-serif;font-size:17px;color:var(--green);line-height:1.1}
  .product__strength{font-family:"Roboto",sans-serif;font-weight:700;font-size:28px;line-height:1.05}
  .product__name{font-family:"Great Vibes",cursive;font-size:40px;line-height:.95}
  .meta{position:absolute;top:262px;width:100%;text-align:center;
    font-family:"Roboto Condensed",sans-serif;font-size:11.5px;color:var(--green);line-height:1.35}
  .volume{position:absolute;left:50%;bottom:12px;transform:translateX(-50%);width:200px;height:24px;
    border-radius:12px;background:var(--pill);color:#fff;display:flex;align-items:center;justify-content:center;gap:10px}
  .volume__mg{font-family:"Tinos",serif;font-size:15px}
  .volume__size{font-family:"Roboto Condensed",sans-serif;font-size:10px}

  /* right panel */
  .facts{position:absolute;left:20px;top:30px;width:190px;border:1px solid var(--green-line);
    border-collapse:collapse;font-size:10.5px}
  .facts td{border-top:1px solid var(--green-line);padding:3px 5px;vertical-align:top;line-height:1.3}
  .facts tr:first-child td{border-top:0}
  .facts .facts__head{font-weight:700;font-size:11.5px}
  .facts .facts__sub{font-weight:400;font-size:10.5px}
  .facts .facts__key{font-weight:700;width:62px}
  .note{position:absolute;left:20px;top:190px;font-family:"Tinos",serif;font-size:10.5px;line-height:1.2}
  .note strong{font-weight:400;text-transform:uppercase;display:block}
  .code{position:absolute;right:4px;top:30px;height:230px;writing-mode:vertical-rl;transform:rotate(180deg);
    font-family:"Roboto Condensed",sans-serif;font-size:10.5px;letter-spacing:.3px;text-align:right}
</style>
</head>
<body>
<main class="canvas">

  <section class="label label--left">
    <div class="info">
      <h3>Calm for body and mind</h3>
      <p>Helps ease mental and emotional stress, tension and worry. Omega fatty acids support mood and brain function, so you feel alert and focused.</p>
      <h3>Restful sleep</h3>
      <p>Take 2–3 hours before bedtime to feel relaxed and ready for a good night's sleep.</p>
      <h4>Eases chronic pain and inflammation</h4>
      <h4>Natural, non-addictive relief</h4>
    </div>
    <div class="splash splash--side" role="img" aria-label="Soft teal watercolour splash"></div>
    <span class="label__pill"></span>
  </section>

  <section class="label label--front">
    <div class="brand">
      <span class="brand__dot"></span>
      <span class="brand__name">Marbleleaf Hemp</span>
    </div>
    <span class="brand__tag">Zero THC</span>
    <div class="splash splash--front" role="img" aria-label="Teal watercolour splash behind product name"></div>
    <div class="product">
      <p class="product__line">Premium</p>
      <p class="product__line">Full Spectrum</p>
      <p class="product__strength">2000</p>
      <p class="product__name">Hemp Oil</p>
    </div>
    <div class="meta">
      <p>Natural Peppermint Flavor</p>
      <p>Dietary Supplement</p>
    </div>
    <div class="volume">
      <span class="volume__mg">2000 mg</span>
      <span class="volume__size">1FLOZ(30ML)</span>
    </div>
  </section>

  <section class="label label--right">
    <table class="facts">
      <tr><td colspan="2" class="facts__head">Supplement Facts<br><span class="facts__sub">Serving Size 1 mL<br>Servings per bottle 30</span></td></tr>
      <tr><td class="facts__key">Hemp Oil</td><td>2000 mg per bottle</td></tr>
      <tr><td class="facts__key">Flavor</td><td>Natural peppermint</td></tr>
      <tr><td colspan="2">Full spectrum, zero THC</td></tr>
      <tr><td colspan="2">Omega fatty acids support mood<br>and overall brain function.</td></tr>
    </table>
    <p class="note"><strong>Directions</strong>Take 1 mL under the tongue,<br>2–3 hours before bedtime.</p>
    <p class="code">KEEP OUT OF REACH OF CHILDREN &nbsp;LOT 2537879</p>
    <span class="label__pill"></span>
  </section>

</main>
</body>
</html>
```